Loan broker seeks referral card design for real estate financing

We need a design for a referral card for people who recommend us for real estate financing. If the deal goes through, each referrer will receive €750.

Text similar to: Recommend me! For every successful real estate financing referral, you will receive €750. (Other suggestions are also welcome)

The size should be no larger than A5 format, or possibly even oblong.
The design should convey security and competence and include themes such as independent advice.

The design should also include the company logo and a photo of me. Naturally, the design should also include a link to my website: www.die-wandlinger.at, along with my phone number and email address: office@die-wandlinger.at

```html
<!DOCTYPE html>
<html lang="de">
<head>
<meta charset="utf-8">
<title>Empfehlungskarte – Wandlinger Finanz GmbH</title>
<link rel="stylesheet" href="https://fonts.googleapis.com/css2?family=Quicksand:wght@500;700&family=Pinyon+Script&display=swap">
<style>
  :root {
    --brand-blue: #2a5aa8;
    --text-grey: #636363;
    --wave-grey: #6b6b6b;
    --paper: #f9f9f9;
    --backdrop: #e6e6e6;
    --white: #ffffff;
  }
  * { margin: 0; padding: 0; box-sizing: border-box; }
  html, body {
    width: 1200px; height: 1124px; overflow: hidden;
    background: var(--backdrop);
    font-family: "Quicksand", "Helvetica Neue", Arial, sans-serif;
  }
  .referral-card {
    position: absolute; left: 0; top: 139px;
    width: 1200px; height: 846px;
    background: var(--brand-blue);
    overflow: hidden;
  }
  .card-background { position: absolute; inset: 0; width: 100%; height: 100%; }
  .brand-block { position: absolute; left: 612px; top: 49px; height: 152px; display: flex; align-items: center; }
  .brand-ring {
    width: 150px; height: 150px; border-radius: 50%;
    border: 5px solid var(--white);
  }
  .brand-divider { width: 4px; height: 152px; background: var(--white); margin-left: 14px; margin-right: 12px; }
  .brand-text { color: var(--white); }
  .brand-name { font-size: 27px; font-weight: 700; line-height: 1.1; }
  .brand-tagline { font-size: 19px; font-weight: 700; margin-top: 8px; }
  .invitation {
    position: absolute; left: 72px; top: 150px;
    font-family: "Pinyon Script", cursive;
    color: var(--brand-blue); font-size: 56px; line-height: 68px;
    font-weight: 400;
  }
  .invitation span { display: block; }
  .invitation .second { padding-left: 24px; }
  .offer {
    position: absolute; left: 57px; top: 300px;
    color: var(--text-grey); font-weight: 700;
    font-size: 49px; line-height: 67px;
  }
  .reward {
    position: absolute; left: 56px; top: 512px;
    color: var(--brand-blue); font-weight: 700;
    font-size: 88px; line-height: 1;
  }
  .contact-list { position: absolute; left: 57px; top: 627px; list-style: none; }
  .contact-item {
    display: flex; align-items: center; height: 42px; margin-bottom: 21px;
    color: var(--text-grey); font-weight: 700; font-size: 33px;
  }
  .contact-icon {
    width: 41px; height: 41px; border-radius: 50%; background: var(--brand-blue);
    display: flex; align-items: center; justify-content: center; margin-right: 13px; flex: none;
  }
  .contact-icon svg { width: 22px; height: 22px; }
  .advisor-portrait {
    position: absolute; left: 728px; top: 212px; width: 472px; height: 634px;
    border-radius: 220px 220px 0 0;
    background: linear-gradient(180deg, #c49a86 0%, #d9ad98 35%, #4a4658 62%, #2e2c3a 100%);
  }
</style>
</head>
<body>
<main class="referral-card">
  <svg class="card-background" viewBox="0 0 1606 1132" preserveAspectRatio="none" aria-hidden="true">
    <path fill="var(--wave-grey)" d="M0,160 C150,95 300,78 420,98 C560,125 700,220 850,340 C950,420 1050,470 1120,505 C1250,580 1400,598 1606,578 L1606,1132 L0,1132 Z"/>
    <path fill="var(--white)" d="M0,168 C150,103 300,86 420,108 C560,140 700,240 845,360 C950,445 1060,520 1140,560 C1270,625 1420,640 1606,628 L1606,1132 L0,1132 Z"/>
    <path fill="var(--wave-grey)" d="M1220,610 C1330,640 1450,648 1606,640 L1606,690 C1450,700 1320,690 1220,660 Z"/>
    <path fill="var(--paper)" d="M0,176 C150,111 300,94 420,116 C560,148 700,250 845,372 C950,460 1060,545 1150,600 C1280,690 1420,700 1606,692 L1606,1132 L0,1132 Z"/>
  </svg>

  <div class="brand-block">
    <div class="brand-ring"></div>
    <div class="brand-divider"></div>
    <div class="brand-text">
      <div class="brand-name">Wandlinger Finanz GmbH</div>
      <div class="brand-tagline">Finanzieren, Versichern, Vorsorgen</div>
    </div>
  </div>

  <h1 class="invitation"><span>Empfehlen Sie</span><span class="second">mich weiter!</span></h1>

  <p class="offer">Für jede realisierte<br>Immobilienfinanzierung<br>erhalten Sie als Tippgeber</p>
  <p class="reward">€ 750</p>

  <ul class="contact-list">
    <li class="contact-item">
      <span class="contact-icon"><svg viewBox="0 0 24 24"><path fill="#fff" d="M6.6 10.8a15.1 15.1 0 0 0 6.6 6.6l2.2-2.2c.3-.3.7-.4 1-.2 1.1.4 2.3.6 3.6.6.6 0 1 .4 1 1V20c0 .6-.4 1-1 1A17 17 0 0 1 3 4c0-.6.4-1 1-1h3.5c.6 0 1 .4 1 1 0 1.3.2 2.5.6 3.6.1.3 0 .7-.2 1z"/></svg></span>
      (123) 555 018
    </li>
    <li class="contact-item">
      <span class="contact-icon"><svg viewBox="0 0 24 24"><rect x="3" y="6" width="18" height="12" rx="1" fill="none" stroke="#fff" stroke-width="2"/><path d="M3 7l9 6 9-6" fill="none" stroke="#fff" stroke-width="2"/></svg></span>
      office@die-wandlinger.at
    </li>
    <li class="contact-item">
      <span class="contact-icon"><svg viewBox="0 0 24 24" fill="none" stroke="#fff" stroke-width="1.8"><circle cx="12" cy="12" r="9"/><ellipse cx="12" cy="12" rx="4" ry="9"/><path d="M3 12h18M4.5 7.5h15M4.5 16.5h15"/></svg></span>
      www.die-wandlinger.at
    </li>
  </ul>

  <div class="advisor-portrait" role="img" aria-label="Porträtfoto des Finanzberaters im dunklen Sakko mit weißem Hemd"></div>
</main>
</body>
</html>
```